Book Cover for self help book describing how to become the author of your life

I need a good resolution front cover for a book that is published through Brelvox in Print and ebook format. I can design the spine and back cover myself so just need the front angle.
The book is titled "Paint Tomorrow Bright" and it's about writing your own story for how you want to live your life. The image I had in my mind was a pen writing out the title on the front in a script-like font, like actual handwriting.
I've included a very basic mock-up that I've done myself just to give the general idea. The cover requires three pieces of writing.
Title: Paint Tomorrow Bright
Subtitle: Walk Along the Quiet Harbour Path
Author: Martin Folwell
Female 35-55

```html
<!DOCTYPE html>
<html lang="en">
<head>
<meta charset="utf-8">
<title>Paint Tomorrow Bright — Martin Folwell</title>
<link rel="stylesheet" href="https://fonts.googleapis.com/css2?family=Kaushan+Script&family=Permanent+Marker&display=swap">
<style>
  :root {
    --backdrop: #e4e5e0;
    --paper: #fbfbf9;
    --paper-shade: #e6e6e3;
    --kraft: #a88468;
    --kraft-dark: #8a6a52;
    --title-ink: #7a4a35;
    --ink: #141414;
    --skin: #e9b9a0;
  }
  * { box-sizing: border-box; margin: 0; padding: 0; }
  html, body {
    width: 1200px;
    height: 1200px;
    overflow: hidden;
    background: var(--backdrop);
  }
  .cover {
    position: absolute;
    left: 205px;
    top: 40px;
    width: 790px;
    height: 1120px;
    background: var(--paper);
    overflow: hidden;
    box-shadow: 0 2px 6px rgba(0,0,0,0.08);
  }
  .cover-bands {
    position: absolute;
    inset: 0;
    width: 790px;
    height: 1120px;
  }
  .title {
    position: absolute;
    left: 0;
    top: 70px;
    width: 710px;
    text-align: center;
    font-family: "Kaushan Script", cursive;
    font-size: 74px;
    line-height: 1;
    color: var(--title-ink);
    opacity: 0.85;
    white-space: nowrap;
  }
  .subtitle {
    position: absolute;
    font-family: "Kaushan Script", cursive;
    color: var(--ink);
    white-space: nowrap;
    line-height: 1;
  }
  .subtitle-lead { left: 150px; top: 355px; font-size: 88px; }
  .subtitle-key {
    left: 325px; top: 510px;
    font-family: "Permanent Marker", cursive;
    font-size: 40px;
    letter-spacing: 1px;
  }
  .subtitle-tail { left: 355px; top: 585px; font-size: 66px; }
  .hand-with-pen {
    position: absolute;
    left: 0;
    top: 468px;
    width: 280px;
    height: 412px;
    background: linear-gradient(100deg, var(--skin) 0%, #f2cdb8 55%, rgba(251,251,249,0) 100%);
    border-radius: 0 140px 120px 0;
  }
  .ink-splatter {
    position: absolute;
    left: 150px;
    top: 700px;
    width: 515px;
    height: 135px;
    background: radial-gradient(ellipse at center, rgba(20,20,20,0.12), rgba(20,20,20,0) 70%);
  }
  .author {
    position: absolute;
    left: 85px;
    top: 990px;
    width: 628px;
    text-align: center;
    font-family: "Kaushan Script", cursive;
    font-size: 54px;
    line-height: 1;
    color: var(--ink);
    white-space: nowrap;
  }
</style>
</head>
<body>
  <main class="cover">
    <svg class="cover-bands" viewBox="0 0 790 1120" aria-hidden="true">
      <defs>
        <linearGradient id="curl" x1="0" x2="1" y1="0" y2="0">
          <stop offset="0" stop-color="#ffffff"/>
          <stop offset="0.6" stop-color="var(--paper-shade)"/>
          <stop offset="1" stop-color="#c9c9c5"/>
        </linearGradient>
        <linearGradient id="curl-left" x1="1" x2="0" y1="0" y2="0">
          <stop offset="0" stop-color="#ffffff"/>
          <stop offset="0.6" stop-color="var(--paper-shade)"/>
          <stop offset="1" stop-color="#c9c9c5"/>
        </linearGradient>
      </defs>
      <!-- top torn band -->
      <path class="band band-top" fill="var(--kraft)"
        d="M0 40 L40 36 L80 42 L120 35 L170 41 L220 34 L270 40 L320 35 L370 42 L420 36 L470 41 L520 34 L570 40 L620 36 L670 41 L710 36
           L710 228 L670 234 L620 227 L570 235 L520 229 L470 236 L420 228 L370 234 L320 227 L270 235 L220 229 L170 236 L120 228 L70 234 L30 227 L0 232 Z"/>
      <path d="M0 40 L40 36 L80 42 L120 35 L170 41 L220 34 L270 40 L320 35 L370 42 L420 36 L470 41 L520 34 L570 40 L620 36 L670 41 L710 36"
        fill="none" stroke="var(--kraft-dark)" stroke-width="3" opacity="0.5"/>
      <path d="M710 36 Q760 40 770 70 L770 268 Q760 280 730 272 L710 228 Z" fill="url(#curl)"/>
      <!-- bottom torn band -->
      <path class="band band-bottom" fill="var(--kraft)"
        d="M85 963 L130 958 L180 965 L230 959 L280 966 L330 960 L380 965 L430 958 L480 964 L530 959 L580 966 L630 960 L680 964 L713 960
           L713 1083 L680 1088 L630 1081 L580 1089 L530 1082 L480 1088 L430 1080 L380 1087 L330 1081 L280 1088 L230 1082 L180 1089 L130 1081 L85 1086 Z"/>
      <path d="M85 963 L85 1086 L48 1096 Q35 1060 40 980 Q55 962 85 963 Z" fill="url(#curl-left)"/>
      <path d="M713 960 Q745 962 752 985 L752 1095 Q740 1105 713 1083 Z" fill="url(#curl)"/>
    </svg>

    <h1 class="title">Paint Tomorrow Bright</h1>

    <div class="hand-with-pen" role="img" aria-label="Photograph of a hand holding a fountain pen, writing on the page"></div>

    <p class="subtitle subtitle-lead">Walk Along the</p>
    <p class="subtitle subtitle-key">QUIET</p>
    <p class="subtitle subtitle-tail">Harbour Path</p>

    <div class="ink-splatter" role="img" aria-label="Scattered drops of black ink"></div>

    <p class="author">Martin Folwell</p>
  </main>
</body>
</html>
```